Motorcycle Shop Business Card

New business card for Motorcycle repair and customization shop.Business name: Copper Falcon Chris Morris443-865-5190, 7214 Quarry Lane Arbutus, MD 21227. www.dale@copperfalconcustoms.example. I uploaded some motorcycle images and logo and a couple of our calendar shoots. They do not have to be used on card just examples of some of our work and past graphic work.
We work on Vantor Brennick and Custom Built Motorcycles.

Looking for front and back design

Target Market(s)

Motorcycle owners

Industry/Entity Type

Motorcycle Part

```html
<!DOCTYPE html>
<html lang="en">
<head>
<meta charset="utf-8">
<title>Copper Falcon – Business Card</title>
<link href="https://fonts.googleapis.com/css2?family=Montserrat:wght@500;600;700&display=swap" rel="stylesheet">
<style>
  :root {
    --canvas: #e9e0e1;
    --frame: #1c1919;
    --card: #ffffff;
    --ink: #1b1b1b;
    --accent: #a8281b;
  }
  * { margin: 0; padding: 0; box-sizing: border-box; }
  html, body { width: 1200px; height: 1200px; overflow: hidden; }
  body {
    background: var(--canvas);
    font-family: "Montserrat", Arial, sans-serif;
    color: var(--ink);
    position: relative;
  }
  .card {
    position: absolute;
    left: 267px;
    width: 708px;
    height: 404px;
    background: var(--frame);
    padding: 22px;
  }
  .card--front { top: 132px; }
  .card--back { top: 666px; }
  .card__face {
    position: relative;
    width: 100%;
    height: 100%;
    background: var(--card);
    box-shadow: 0 0 8px rgba(140,140,140,0.7);
    overflow: hidden;
  }
  .photo {
    position: absolute;
    border-radius: 6px;
  }
  .photo--front-bike {
    left: 10px; top: 80px; width: 326px; height: 266px;
    background:
      radial-gradient(ellipse 55% 45% at 42% 55%, rgba(120,30,30,0.55), rgba(120,30,30,0) 70%),
      linear-gradient(160deg, #d9dbde 0%, #8d9096 30%, #2a2425 58%, #151213 80%, #a6a9ae 100%);
  }
  .photo--back-bike {
    left: 354px; top: 128px; width: 310px; height: 212px;
    background:
      radial-gradient(ellipse 45% 40% at 60% 30%, rgba(150,205,225,0.8), rgba(150,205,225,0) 70%),
      linear-gradient(200deg, #eef3f5 0%, #c9d6db 35%, #7e8488 65%, #2b2b2e 85%, #b8bcc0 100%);
  }
  .brand {
    position: absolute;
    display: flex;
    align-items: center;
    justify-content: center;
    gap: 14px;
    font-weight: 700;
    color: var(--ink);
    white-space: nowrap;
  }
  .brand__dot {
    flex: 0 0 auto;
    background: var(--accent);
    border-radius: 50%;
  }
  .brand__name { line-height: 1.02; text-align: center; letter-spacing: 1px; }
  .brand--large { left: 222px; top: 46px; width: 408px; }
  .brand--large .brand__name { font-size: 36px; }
  .brand--large .brand__dot { width: 22px; height: 22px; }
  .tagline {
    position: absolute;
    left: 280px; top: 140px; width: 290px;
    text-align: center;
    color: var(--accent);
    font-weight: 600;
    font-size: 13px;
    line-height: 1.3;
  }
  .holder__name {
    position: absolute;
    left: 19px; top: 18px;
    font-size: 42px;
    font-weight: 700;
    letter-spacing: 0.5px;
    white-space: nowrap;
  }
  .holder__role {
    position: absolute;
    left: 152px; top: 74px;
    font-size: 14px;
    font-weight: 500;
    letter-spacing: 0.5px;
  }
  .brand--small { left: 93px; top: 208px; width: 193px; gap: 10px; }
  .brand--small .brand__name { font-size: 17px; }
  .brand--small .brand__dot { width: 12px; height: 12px; }
  .contact {
    position: absolute;
    left: 20px; top: 266px; width: 340px;
    text-align: center;
    font-style: normal;
    font-size: 16px;
    font-weight: 500;
    line-height: 1.45;
  }
</style>
</head>
<body>
  <section class="card card--front">
    <div class="card__face">
      <div class="photo photo--front-bike" role="img" aria-label="Photo of a black cruiser motorcycle with red flame paint and chrome details"></div>
      <div class="brand brand--large"><span class="brand__dot"></span><span class="brand__name">COPPER<br>FALCON</span></div>
      <p class="tagline">motorcycle<br>repair &amp; customization</p>
    </div>
  </section>

  <section class="card card--back">
    <div class="card__face">
      <h1 class="holder__name">DALE FENWICK</h1>
      <p class="holder__role">OWNER</p>
      <div class="brand brand--small"><span class="brand__dot"></span><span class="brand__name">COPPER<br>FALCON</span></div>
      <address class="contact">
        410-555-0137<br>
        7214 Quarry Lane Arbutus, MD 21227
      </address>
      <div class="photo photo--back-bike" role="img" aria-label="Photo of a white custom chopper with light blue flame graphics and chrome front wheel"></div>
    </div>
  </section>
</body>
</html>
```